SEO AND WEB DESIGN COMPANY BUSINESS CARD DESIGN

I need an eye catching , simple business card design that will match my logo . I need 2 versions of it ( white background and black background) - SOME PEOPLE DID NOT GET IT AND SENDING US FRONT WHITE BACK WHITE VERSIONS WHICH IS NOT CORRECT.

ONE VERSION SHOULD BE BACK AND FRONT ALL BLACK , SECOND VERSION SHOULD BE BACK AND FRONT ALL WHITE

logo psd files are attached for both versions. The business card is going to have : First Name- Last name - position - phone numbers

```html
<!DOCTYPE html>
<html lang="en">
<head>
<meta charset="utf-8">
<title>Northrise Business Card – Black Version</title>
<link rel="stylesheet" href="https://fonts.googleapis.com/css2?family=Oswald:wght@500&family=Source+Sans+3:wght@400&family=Nunito+Sans:wght@300&display=swap">
<style>
  :root {
    --backdrop: #e7e4df;
    --card: #1f1f20;
    --white: #ffffff;
    --blue: #3f86c8;
    --grey: #7a7a7a;
    --shadow: rgba(0, 0, 0, 0.35);
  }
  html, body {
    margin: 0;
    padding: 0;
    width: 1200px;
    height: 960px;
    overflow: hidden;
    background: var(--backdrop);
  }
  .canvas {
    position: relative;
    width: 1200px;
    height: 960px;
  }
  .card {
    position: absolute;
    background: var(--card);
    box-shadow: 0 6px 14px var(--shadow);
    overflow: hidden;
  }
  .card-front {
    left: 272px;
    top: 86px;
    width: 660px;
    height: 392px;
  }
  .card-back {
    left: 274px;
    top: 500px;
    width: 658px;
    height: 390px;
  }

  /* Front: brand lockup */
  .brand {
    position: absolute;
    left: 0;
    right: 0;
    top: 150px;
    display: flex;
    flex-direction: column;
    align-items: center;
  }
  .brand-row {
    display: flex;
    align-items: center;
    gap: 12px;
  }
  .brand-dot {
    width: 26px;
    height: 26px;
    border-radius: 50%;
    background: var(--blue);
  }
  .brand-name {
    font-family: "Oswald", sans-serif;
    font-weight: 500;
    font-size: 50px;
    line-height: 1;
    letter-spacing: 1px;
    color: var(--white);
  }
  .brand-tagline {
    display: flex;
    align-items: center;
    gap: 6px;
    margin-top: 6px;
    font-family: "Oswald", sans-serif;
    font-weight: 500;
    font-size: 9.5px;
    letter-spacing: 4.6px;
    color: var(--white);
  }
  .brand-tagline .rule {
    width: 26px;
    height: 1.5px;
    background: var(--blue);
  }

  /* Back: decoration */
  .back-ornament {
    position: absolute;
    left: 0;
    top: 0;
  }

  /* Back: identity */
  .person-name {
    position: absolute;
    left: 356px;
    top: 56px;
    margin: 0;
    font-family: "Source Sans 3", sans-serif;
    font-weight: 400;
    font-size: 34px;
    line-height: 1;
    color: var(--white);
  }
  .name-rule {
    position: absolute;
    left: 398px;
    top: 97px;
    width: 260px;
    height: 3px;
    background: linear-gradient(to right, rgba(63, 134, 200, 0), var(--blue) 35%);
  }
  .person-title {
    position: absolute;
    right: 112px;
    top: 107px;
    margin: 0;
    font-family: "Source Sans 3", sans-serif;
    font-weight: 400;
    font-size: 20px;
    line-height: 1;
    color: var(--white);
  }
  .contact {
    position: absolute;
    left: 380px;
    top: 254px;
    margin: 0;
    padding: 0;
    list-style: none;
    font-family: "Nunito Sans", sans-serif;
    font-weight: 300;
    font-size: 21px;
    line-height: 29px;
    color: var(--white);
  }
</style>
</head>
<body>
<main class="canvas">

  <section class="card card-front" aria-label="Card front">
    <div class="brand">
      <div class="brand-row">
        <span class="brand-dot"></span>
        <span class="brand-name">NORTHRISE</span>
      </div>
      <div class="brand-tagline">
        <span class="rule"></span>
        <span>DESIGN &amp; MARKETING</span>
        <span class="rule"></span>
      </div>
    </div>
  </section>

  <section class="card card-back" aria-label="Card back">
    <svg class="back-ornament" width="658" height="390" viewBox="0 0 658 390" aria-hidden="true">
      <circle cx="134" cy="226" r="104" fill="none" stroke="var(--grey)" stroke-width="22"/>
    </svg>

    <h1 class="person-name">Daniel Moore</h1>
    <div class="name-rule"></div>
    <p class="person-title">President</p>

    <ul class="contact">
      <li>phone: (xx) xxx-xxxxx</li>
      <li>phone: (xx) xxx-xxxxx</li>
    </ul>
  </section>

</main>
</body>
</html>
```